Brivolo ( A new twist on task management )

We need modern, elegant, and clean (Quillon Design) on screens, buttons, and icons.

It is a (smart) task management application which helps the users to get notified and track task completion hassle free; Using notification profiles they create.

The interface of this application should be very simple and color schemes should be contemporary as long as they don’t make reading short text hard.

Following Quillon Design guidelines, the prefered font style is Roboto

Target Market(s)

Everyone from 13+

Industry/Entity Type

Software

Logo Text

Brivolo

Font styles to use
Other font styles liked:
• Roboto

```html
<!DOCTYPE html>
<html lang="en">
<head>
<meta charset="utf-8">
<title>Brivolo – Active Tasks</title>
<link href="https://fonts.googleapis.com/css2?family=Roboto:wght@400;500;700&display=swap" rel="stylesheet">
<style>
  :root {
    --page-bg: #f2f4f7;
    --navy: #0d2a6e;
    --navy-deep: #09225c;
    --ink: #0f2b66;
    --subbar: #cfe0ea;
    --row-bg: #e3f3fc;
    --row-line: #8ea7c2;
    --accent: #1e9be0;
    --action-bar: #06baf0;
    --white: #ffffff;
    --status-ink: #111111;
  }
  * { box-sizing: border-box; margin: 0; padding: 0; }
  html, body { width: 831px; height: 1200px; overflow: hidden; }
  body { background: var(--page-bg); font-family: "Roboto", sans-serif; color: var(--ink); }

  .app-screen { position: absolute; left: 77px; top: 0; width: 676px; height: 1200px; background: var(--row-bg); overflow: hidden; }

  .status-bar { position: absolute; left: 0; top: 0; width: 100%; height: 25px; background: var(--white); color: var(--status-ink); font-size: 16px; display: flex; align-items: center; justify-content: space-between; padding: 0 14px; }
  .status-bar .time { position: absolute; left: 50%; transform: translateX(-50%); font-weight: 500; }
  .status-bar .carrier, .status-bar .power { display: flex; align-items: center; gap: 6px; }

  .profile-header { position: absolute; left: 0; top: 25px; width: 100%; height: 231px; background: var(--navy); text-align: center; color: var(--white); }
  .profile-avatar { position: absolute; left: 296px; top: 34px; width: 84px; height: 84px; border-radius: 50%; border: 4px solid var(--white); background: radial-gradient(circle at 40% 55%, #f3a3c0, #d63a67 55%, #7a1c3a); }
  .profile-name { position: absolute; top: 147px; width: 100%; font-size: 32px; font-weight: 500; }
  .profile-location { position: absolute; top: 187px; width: 100%; font-size: 23px; font-weight: 400; color: #dbe4f5; }

  .add-button { position: absolute; left: 567px; top: 208px; width: 80px; height: 80px; border-radius: 50%; background: var(--accent); box-shadow: 0 3px 8px rgba(0,0,0,.3); z-index: 3; display: flex; align-items: center; justify-content: center; }

  .section-bar { position: absolute; left: 0; top: 256px; width: 100%; height: 66px; background: var(--subbar); display: flex; align-items: center; }
  .back-link { position: absolute; left: 50px; display: flex; align-items: center; gap: 10px; font-size: 24px; color: var(--ink); }
  .section-title { width: 100%; text-align: center; font-size: 30px; letter-spacing: .5px; color: var(--ink); }

  .task-list { position: absolute; left: 0; top: 322px; width: 100%; list-style: none; }
  .task-row { position: relative; background: var(--row-bg); border-bottom: 2px solid var(--row-line); }
  .task-row .play { position: absolute; left: 58px; }
  .task-name { position: absolute; left: 106px; font-size: 30px; color: var(--ink); }
  .task-icons { position: absolute; right: 0; top: 0; height: 100%; }
  .task-icons svg { position: absolute; }
  .icon-pin { left: -189px; }
  .icon-clock { left: -115px; }
  .icon-place { left: -44px; }
  .task-row.running .task-name { font-weight: 700; }
  .timer { position: absolute; left: 106px; font-size: 21px; font-weight: 700; color: var(--ink); }

  .search-bar { position: absolute; left: 0; top: 1107px; width: 100%; height: 93px; background: var(--action-bar); display: flex; justify-content: center; align-items: center; }
</style>
</head>
<body>
<main class="app-screen">
  <div class="status-bar">
    <span class="carrier">●●●○○ phone
      <svg width="20" height="14" viewBox="0 0 20 14"><path d="M10 13 3 6a10 10 0 0 1 14 0z" fill="#111"/></svg>
    </span>
    <span class="time">4:21 PM</span>
    <span class="power">
      <svg width="10" height="16" viewBox="0 0 10 16"><path d="M1 4l8 8-4 3V1l4 3-8 8" fill="none" stroke="#111" stroke-width="1.5"/></svg>
      100%
      <svg width="40" height="16" viewBox="0 0 40 16"><rect x="1" y="1" width="34" height="14" rx="2" fill="#111"/><rect x="36" y="5" width="3" height="6" fill="#111"/></svg>
    </span>
  </div>

  <header class="profile-header">
    <div class="profile-avatar" role="img" aria-label="Profile photo of the user"></div>
    <p class="profile-name">Daniel Marsh</p>
    <p class="profile-location">Northbury, United Kingdom</p>
  </header>

  <div class="add-button" aria-label="Add task">
    <svg width="36" height="36" viewBox="0 0 36 36"><path d="M18 5v26M5 18h26" stroke="#fff" stroke-width="5" stroke-linecap="round"/></svg>
  </div>

  <nav class="section-bar">
    <span class="back-link">
      <svg width="14" height="24" viewBox="0 0 14 24"><path d="M12 2 3 12l9 10" fill="none" stroke="#0f2b66" stroke-width="3"/></svg>
      Back
    </span>
    <h1 class="section-title" style="font-weight:400">ACTIVE TASKS</h1>
  </nav>

  <svg width="0" height="0" style="position:absolute">
    <defs>
      <symbol id="play" viewBox="0 0 16 24"><path d="M2 2l12 10L2 22z" fill="#0f2b66"/></symbol>
      <symbol id="pin" viewBox="0 0 40 40"><path d="M22 4l14 14-4 2-6 6 1 8-3 2-8-9-10 10-2-2 10-10-9-8 2-3 8 1 6-6z" fill="#0f2b66"/></symbol>
      <symbol id="clock" viewBox="0 0 40 40"><circle cx="20" cy="20" r="16" fill="none" stroke="#0f2b66" stroke-width="3.5"/><path d="M20 10v11h8" fill="none" stroke="#0f2b66" stroke-width="3.5"/></symbol>
      <symbol id="place" viewBox="0 0 40 40"><path d="M20 37S7 23 7 15a13 13 0 0 1 26 0c0 8-13 22-13 22z" fill="none" stroke="#0f2b66" stroke-width="3.5"/><circle cx="20" cy="15" r="4.5" fill="#0f2b66"/></symbol>
    </defs>
  </svg>

  <ul class="task-list">
    <li class="task-row" style="height:130px">
      <svg class="play" style="top:51px" width="16" height="24"><use href="#play"/></svg>
      <span class="task-name" style="top:46px">01 Task</span>
      <span class="task-icons">
        <svg class="icon-pin" style="top:46px" width="38" height="38"><use href="#pin"/></svg>
        <svg class="icon-clock" style="top:46px" width="40" height="40"><use href="#clock"/></svg>
        <svg class="icon-place" style="top:44px" width="40" height="42"><use href="#place"/></svg>
      </span>
    </li>
    <li class="task-row running" style="height:173px">
      <svg class="play" style="top:52px" width="22" height="22"><rect width="22" height="22" fill="#0f2b66"/></svg>
      <span class="task-name" style="top:44px">01 Task</span>
      <svg style="position:absolute;left:58px;top:103px" width="16" height="26"><rect x="2" width="4" height="26" fill="#0f2b66"/><rect x="10" width="4" height="26" fill="#0f2b66"/></svg>
      <span class="timer" style="top:104px">00:15:30</span>
      <span class="task-icons">
        <svg class="icon-place" style="top:44px" width="40" height="42"><use href="#place"/></svg>
      </span>
    </li>
    <li class="task-row" style="height:172px">
      <svg class="play" style="top:74px" width="16" height="24"><use href="#play"/></svg>
      <span class="task-name" style="top:68px">01 Task</span>
      <span class="task-icons">
        <svg class="icon-pin" style="top:68px" width="38" height="38"><use href="#pin"/></svg>
        <svg class="icon-place" style="top:66px" width="40" height="42"><use href="#place"/></svg>
      </span>
    </li>
    <li class="task-row" style="height:184px">
      <svg class="play" style="top:80px" width="16" height="24"><use href="#play"/></svg>
      <span class="task-name" style="top:74px">01 Task</span>
      <span class="task-icons">
        <svg class="icon-pin" style="top:74px" width="38" height="38"><use href="#pin"/></svg>
        <svg class="icon-clock" style="top:74px" width="40" height="40"><use href="#clock"/></svg>
      </span>
    </li>
    <li class="task-row" style="height:130px;border-bottom:0">
      <svg class="play" style="top:78px" width="16" height="24"><use href="#play"/></svg>
      <span class="task-name" style="top:72px">01 Task</span>
      <span class="task-icons">
        <svg class="icon-pin" style="top:72px" width="38" height="38"><use href="#pin"/></svg>
        <svg class="icon-clock" style="top:72px" width="40" height="40"><use href="#clock"/></svg>
        <svg class="icon-place" style="top:70px" width="40" height="42"><use href="#place"/></svg>
      </span>
    </li>
  </ul>

  <footer class="search-bar" aria-label="Search">
    <svg width="66" height="66" viewBox="0 0 66 66"><circle cx="26" cy="26" r="17" fill="none" stroke="#fff" stroke-width="7"/><path d="M38 38l20 20" stroke="#fff" stroke-width="9" stroke-linecap="round"/></svg>
  </footer>
</main>
</body>
</html>
```